Design our branded business card!

We'd love for you to design our business card and come up with a fitting design that reflects the Brimble brand. We're a growing tech startup with big ambitions. We've included our brand guidelines (contain colour palette), logo (EPS vector in CMYK) and old designs to help you on your way.

We'd like to keep the design fairly simple:

* Name
* Phone number
* Email address
* Website (www.brimble.life)
* Twitter (@brimble)
* Address (19 Fenwick Row, Leeds, UK, LS4 9QT).

This would need to include print and cutting marks.

If you have any questions just let us know!

Target Market(s)

Businesses, Press and our customers!

Industry/Entity Type

Business

Contact Information for Business Card

* Name
* Phone number
* Email address
* Twitter (@brimble)

Font styles to use
Sans Serif

Requirements
Must have
• 1. Must have the Brimble logo included.
• 2. Must use the font 'Brandon Text' in either 'light' or 'thin' (https://www.typevaultex.com/fonts/qrnfoundry/brandon-text/)
• 3. Must use exact colours references from the brand guidelines. Colours outside of the brand guidelines will be discounted. White (transparent) backgrounds are fine.
• 4. Must contain the following information:
• * Name
• * Phone number
• * Email address
• * Website (www.brimble.life)
• * Twitter (@brimble)
• * Address (19 Fenwick Row, Leeds, UK, LS4 9QT).
Nice to have
• Must use the font 'Brandon Text' in either 'light' or 'thin' (https://www.typevaultex.com/fonts/qrnfoundry/brandon-text/)
Should not have
• Colours outside of the brand guidelines will be discounted. White (transparent) backgrounds are fine.
• Avoid creating icons or including photography.

```html
<!DOCTYPE html>
<html lang="en">
<head>
<meta charset="utf-8">
<title>Brimble Business Card</title>
<link rel="stylesheet" href="https://fonts.googleapis.com/css2?family=PT+Sans:wght@400;700&display=swap">
<style>
  :root {
    --page-bg: #d9d9d9;
    --card-black: #0d0d0d;
    --card-black-soft: #1a1a1a;
    --brand-green: #6cc15c;
    --text-white: #f2f2f2;
    --rule-grey: #333333;
  }
  * { margin: 0; padding: 0; box-sizing: border-box; }
  html, body {
    width: 1200px;
    height: 900px;
    overflow: hidden;
    background: var(--page-bg);
    font-family: "PT Sans", Arial, sans-serif;
  }
  .sheet {
    position: relative;
    width: 1200px;
    height: 900px;
  }
  .card {
    position: absolute;
    left: 250px;
    width: 700px;
    height: 400px;
    background: radial-gradient(ellipse at 60% 40%, var(--card-black-soft), var(--card-black) 75%);
    box-shadow: 0 6px 18px rgba(0,0,0,0.25);
  }
  .card--back { top: 30px; }
  .card--front { top: 470px; }

  .back-wordmark {
    position: absolute;
    inset: 0;
    display: flex;
    align-items: center;
    justify-content: center;
    color: var(--text-white);
    font-size: 72px;
    font-weight: 400;
    letter-spacing: 2px;
  }

  .brand {
    position: absolute;
    left: 345px;
    top: 62px;
    display: flex;
    align-items: center;
    gap: 18px;
  }
  .brand__dot {
    width: 72px;
    height: 72px;
    border-radius: 50%;
    background: var(--brand-green);
  }
  .brand__name {
    color: var(--text-white);
    font-size: 50px;
    font-weight: 400;
    letter-spacing: 1px;
  }

  .holder-name {
    position: absolute;
    left: 70px;
    top: 150px;
    color: var(--brand-green);
    font-size: 21px;
    font-weight: 700;
  }
  .holder-rule {
    position: absolute;
    left: 250px;
    top: 180px;
    width: 400px;
    height: 1px;
    background: var(--rule-grey);
  }

  .contact-rule {
    position: absolute;
    left: 420px;
    top: 245px;
    width: 230px;
    height: 1px;
    background: var(--rule-grey);
  }
  .contacts {
    position: absolute;
    right: 70px;
    top: 256px;
    list-style: none;
    text-align: right;
    color: var(--text-white);
    font-size: 18px;
    line-height: 22px;
  }
  .contacts li {
    display: flex;
    justify-content: flex-end;
    align-items: center;
    gap: 10px;
  }
  .contacts .icon {
    width: 12px;
    height: 12px;
    flex: none;
  }
  .contacts .icon--none { visibility: hidden; }
</style>
</head>
<body>
<main class="sheet">
  <section class="card card--back" aria-label="Business card back">
    <div class="back-wordmark">Brimble</div>
  </section>

  <section class="card card--front" aria-label="Business card front">
    <div class="brand">
      <span class="brand__dot"></span>
      <span class="brand__name">brimble</span>
    </div>

    <p class="holder-name">Mara Ellison</p>
    <span class="holder-rule"></span>

    <span class="contact-rule"></span>
    <ul class="contacts">
      <li>044-987 654 321
        <svg class="icon" viewBox="0 0 12 12"><path d="M2.5 1 L4.5 1 L5.2 3.5 L4 4.5 C4.6 6 6 7.4 7.5 8 L8.5 6.8 L11 7.5 L11 9.5 C11 10.3 10.3 11 9.5 11 C5 11 1 7 1 2.5 C1 1.7 1.7 1 2.5 1 Z" fill="#6cc15c"/></svg>
      </li>
      <li>info@postbox.com
        <svg class="icon" viewBox="0 0 12 12"><rect x="1" y="2.5" width="10" height="7" fill="#6cc15c"/><path d="M1 2.5 L6 6.5 L11 2.5" fill="none" stroke="#0d0d0d" stroke-width="1"/></svg>
      </li>
      <li>www.brimble.life
        <svg class="icon" viewBox="0 0 12 12"><circle cx="6" cy="6" r="5" fill="#6cc15c"/><path d="M1 6 H11 M6 1 C3.5 3.5 3.5 8.5 6 11 M6 1 C8.5 3.5 8.5 8.5 6 11" fill="none" stroke="#0d0d0d" stroke-width="0.8"/></svg>
      </li>
      <li>@brimble
        <svg class="icon" viewBox="0 0 12 12"><rect x="1" y="1" width="10" height="10" rx="1.5" fill="#6cc15c"/></svg>
      </li>
      <li>19 Fenwick Row, Leeds, UK
        <svg class="icon icon--none" viewBox="0 0 12 12"></svg>
      </li>
      <li>LS4 9QT
        <svg class="icon icon--none" viewBox="0 0 12 12"></svg>
      </li>
    </ul>
  </section>
</main>
</body>
</html>
```